New Business Card Design

We need a business card design for a new company based in Sydney called "Quill and Lantern". This is an online buisness which will have an online store providing imported homewares.
We are looking for something that is different, perhaps even in shape and using the logo that was designed by Tarvello Works.

Attached document is a basic example I want to see more creative versions.

Target Market(s)

Homewares, Interior Design

Industry/Entity Type

Business

Contact Information for Business Card

Company Logo
Company Name
Industry area
Name
Position
Phone
Email
Website
Motto

Requirements
Must have
• Logo
Nice to have
• Social website logos - Chatterloop, Glimmerly, Burblet, Clippadoo, Zorvo+

```html
<!DOCTYPE html>
<html lang="en">
<head>
<meta charset="utf-8">
<title>Quill and Lantern – Business Card</title>
<link href="https://fonts.googleapis.com/css2?family=Great+Vibes&family=Montserrat:wght@400;600;700&family=Open+Sans:wght@400&family=Oswald:wght@500&display=swap" rel="stylesheet">
<style>
  :root{
    --backdrop:#b3b3b3;
    --card:#ffffff;
    --ink:#111111;
    --text:#222222;
    --bronze:#a8825e;
    --gold-light:#f3dfa8;
    --gold:#c9962e;
    --copper:#6e3226;
  }
  html,body{margin:0;padding:0;overflow:hidden;}
  body{width:1149px;height:1200px;background:var(--backdrop);position:relative;font-family:"Open Sans",Arial,sans-serif;color:var(--text);}
  .card{position:absolute;width:728px;height:440px;background:var(--card);overflow:hidden;}
  .card--front{left:218px;top:113px;height:439px;}
  .card--back{left:214px;top:638px;}
  .band{position:absolute;left:0;top:0;}

  /* front */
  .brand-mark{position:absolute;left:0;right:0;top:128px;text-align:center;font-family:"Montserrat",sans-serif;font-weight:600;font-size:40px;color:var(--ink);}
  .industry{position:absolute;left:0;right:0;top:302px;text-align:center;font-family:"Montserrat",sans-serif;font-weight:400;font-size:40px;letter-spacing:4px;color:var(--ink);}
  .front-web{position:absolute;left:0;right:0;top:360px;text-align:center;font-size:20px;color:var(--ink);}
  .rule{position:absolute;top:372px;height:3px;width:108px;}
  .rule--left{left:102px;background:linear-gradient(90deg,transparent,var(--gold),var(--copper));}
  .rule--right{left:520px;background:linear-gradient(90deg,var(--copper),var(--gold),transparent);}

  /* back */
  .back-mark{position:absolute;left:38px;width:290px;top:88px;text-align:center;font-family:"Montserrat",sans-serif;font-weight:600;font-size:26px;color:var(--ink);}
  .company{position:absolute;left:38px;width:290px;top:186px;text-align:center;font-family:"Montserrat",sans-serif;line-height:1.15;color:var(--ink);}
  .company__name{font-weight:700;font-size:24px;}
  .company__industry{font-weight:400;font-size:21px;letter-spacing:1px;}
  .socials{position:absolute;left:53px;top:278px;margin:0;padding:0;list-style:none;}
  .socials li{display:flex;align-items:center;height:27px;font-size:18px;}
  .socials .dot{width:17px;height:17px;border-radius:3px;background:var(--bronze);margin-right:16px;}
  .person{position:absolute;left:370px;top:70px;}
  .person__name{font-family:"Oswald",sans-serif;font-weight:500;font-size:29px;color:var(--bronze);margin:0;line-height:1.2;}
  .person__role{font-size:17px;margin-top:8px;}
  .contacts{position:absolute;left:372px;top:209px;margin:0;padding:0;list-style:none;}
  .contacts li{display:flex;align-items:center;height:31.5px;font-size:18.5px;}
  .contacts svg{width:20px;height:20px;margin-right:15px;fill:var(--bronze);}
  .motto{position:absolute;left:380px;width:330px;top:388px;text-align:center;font-family:"Great Vibes",cursive;font-size:30px;color:#fff;white-space:nowrap;}
</style>
</head>
<body>

<section class="card card--front">
  <div class="brand-mark">Quill and Lantern</div>
  <div class="industry">Homewares</div>
  <div class="rule rule--left"></div>
  <div class="front-web">www.quillandlantern.com.au</div>
  <div class="rule rule--right"></div>
  <svg class="band" width="728" height="439" viewBox="0 0 728 439">
    <defs>
      <linearGradient id="frontGold" x1="0" x2="1">
        <stop offset="0" stop-color="#b8862a"/>
        <stop offset=".1" stop-color="#f3dfa8"/>
        <stop offset=".3" stop-color="#c9962e"/>
        <stop offset=".5" stop-color="#6e3226"/>
        <stop offset=".75" stop-color="#c9962e"/>
        <stop offset=".92" stop-color="#fbf3dc"/>
        <stop offset="1" stop-color="#c9962e"/>
      </linearGradient>
    </defs>
    <rect x="0" y="419" width="728" height="20" fill="var(--ink)"/>
    <polygon points="0,419 518,419 490,439 0,439" fill="url(#frontGold)"/>
  </svg>
</section>

<section class="card card--back">
  <div class="back-mark">Quill and Lantern</div>
  <div class="company">
    <div class="company__name">Quill and Lantern</div>
    <div class="company__industry">Homewares</div>
  </div>
  <ul class="socials">
    <li><span class="dot"></span>quillandlantern</li>
    <li><span class="dot"></span>quillandlantern</li>
    <li><span class="dot"></span>@QuillAndLantern1</li>
    <li><span class="dot"></span>quillandlanternhomewares</li>
  </ul>

  <div class="person">
    <h1 class="person__name">Marisol Avery Quinn</h1>
    <div class="person__role">Director / Stylist</div>
  </div>
  <ul class="contacts">
    <li><svg viewBox="0 0 20 20"><path d="M3 6c0-2 3-3 7-3s7 1 7 3v2h-4V6H7v2H3z"/><rect x="4" y="9" width="12" height="8" rx="1"/></svg>+61 400 555 019</li>
    <li><svg viewBox="0 0 20 20"><path d="M2 5h16v10H2z" /><path d="M2 5l8 6 8-6" fill="none" stroke="#fff" stroke-width="1.5"/></svg>Marisol@quillandlantern.com.au</li>
    <li><svg viewBox="0 0 20 20"><circle cx="10" cy="10" r="8"/><path d="M2 10h16M10 2v16M4 5.5h12M4 14.5h12" stroke="#fff" stroke-width="1" fill="none"/><ellipse cx="10" cy="10" rx="3.5" ry="8" fill="none" stroke="#fff" stroke-width="1"/></svg>www.quillandlantern.com.au</li>
  </ul>

  <svg class="band" width="728" height="440" viewBox="0 0 728 440">
    <defs>
      <linearGradient id="backGold" x1="0" x2="1">
        <stop offset="0" stop-color="#f3dfa8"/>
        <stop offset=".25" stop-color="#c9962e"/>
        <stop offset=".75" stop-color="#9a5a33"/>
        <stop offset="1" stop-color="#6e3226"/>
      </linearGradient>
    </defs>
    <rect x="0" y="412" width="360" height="28" fill="var(--ink)"/>
    <polygon points="356,383 728,383 728,440 314,440" fill="url(#backGold)"/>
  </svg>
  <div class="motto">Warmth for every Room</div>
</section>

</body>
</html>
```